galactic arcade 80s vibes - jewelry company

I am looking for someone to build me a website for my jewelry company - I am going for an 80s retro GALACTIC arcade vibe. I want it to feel old school, be brightly colored (purples, greens, etc) encompass planets, stars, or milky way type vibes. My company is called LumoKitt - it is zodiac signs & angel number jewelry. I want the website to open up as galaxy and my logo/name to pop up in the center of the screen and then go to the main page.

Industry/Entity Type

jewelry

Coding

Coded - Design and coding required

Number of Pages Required

1 page

Font styles to use
Other font styles liked:
• retro

Colors
0094D4
00A9DD
6FCCEA
C7EBF8
E9F6FB
00AB8E
00BBA5
67D7C9
C6EFE9
E9F9F6
59FF00
82FF00
B8FF75
E3FFCB
F4FFEA
FFF300
FFF600
FEFA6F
FFFEC7
FFFEE8
FFC000
F8CF3A
FAE287
FDF2CF
FEFAEE
E54698
E96AAD
F1A4CE
F9D9EA
FCEFF6
A7469A
B969AE
D3A5CF
EDDBEB
F8F0F9
6B429C
8869AF
B7A5CE
E3DAEB
F3F0F8

```html
<!DOCTYPE html>
<html lang="en">
<head>
<meta charset="utf-8">
<title>LumoKitt – Zodiac &amp; Angel Number Jewelry</title>
<link href="https://fonts.googleapis.com/css2?family=Russo+One&family=Roboto:wght@400;500;700&display=swap" rel="stylesheet">
<style>
:root{
  --page:#ffffff;
  --ink:#ffffff;
  --muted:#d9cfe6;
  --night:#12041a;
  --night-2:#1b0826;
  --hero-top:#2a0c4e;
  --hero-mid:#4a1c86;
  --violet:#8a14c4;
  --violet-deep:#5b0f7e;
  --orb:#4a0f66;
  --orb-lit:#3a1896;
  --orb-ring:#5b2fd6;
  --lime:#59ff00;
  --card:#22082e;
  --field:#190620;
  --line:#3e2450;
  --display:"Russo One", sans-serif;
  --text:"Roboto", sans-serif;
}
*{box-sizing:border-box;margin:0;padding:0}
html,body{width:1200px;height:3927px;overflow:hidden;background:var(--page)}
body{position:relative;font-family:var(--text);color:var(--ink)}
.abs{position:absolute}

/* splash */
.splash{position:absolute;left:110px;top:98px;width:960px;height:787px;
  background:radial-gradient(ellipse at 55% 50%,#8a4b8e 0%,#4b2a86 30%,#24195e 60%,#0e0c2c 100%);
  display:flex;align-items:center;justify-content:center}
.splash-name{font-family:var(--display);font-size:150px;color:var(--lime);letter-spacing:2px;margin-top:10px}

/* site */
.site{position:absolute;left:110px;top:938px;width:960px;height:2828px;background:
  linear-gradient(180deg,var(--night) 0%,#1a0724 35%,var(--night) 55%,#1c0828 80%,var(--night) 100%);overflow:hidden}
.nav{position:absolute;left:0;top:0;width:960px;height:60px;background:#10030f;z-index:3}
.brand{position:absolute;font-family:var(--display);color:var(--lime);font-size:27px;letter-spacing:1px}
.nav .brand{left:90px;top:15px}
.menu{position:absolute;left:265px;top:22px;display:flex;gap:25px;font-size:12.5px;font-weight:500}
.menu .active{color:#b34bf0}
.search{position:absolute;left:717px;top:22px}
.btn{position:absolute;display:flex;align-items:center;justify-content:center;gap:8px;background:var(--violet);
  border-radius:20px;font-weight:700;font-size:12.5px;color:#fff}
.btn svg{width:12px;height:12px}
.login{left:765px;top:13px;width:104px;height:33px}

.hero{position:absolute;left:0;top:60px;width:960px;height:600px;
  background:radial-gradient(ellipse at 72% 45%,#6a2aa8 0%,var(--hero-mid) 30%,var(--hero-top) 65%,#1a0833 100%)}
.hero-curve{position:absolute;left:0;top:555px;width:960px;height:110px}
.welcome{left:90px;top:230px;font-family:var(--display);font-size:25px;letter-spacing:1px}
.hero-title{left:90px;top:275px;font-family:var(--display);font-size:50px;letter-spacing:1px}
.hero-copy{left:90px;top:338px;width:340px;font-size:12.5px;line-height:21px;color:var(--muted)}
.get-started{left:90px;top:398px;width:140px;height:39px}
.wheel{left:444px;top:100px;width:444px;height:444px;border-radius:50%;
  background:radial-gradient(circle,#fff8d0 0%,#d8c98a 8%,#7c52c8 30%,#5a2aa2 60%,rgba(90,42,162,0.2) 100%)}

h2.section{position:absolute;left:0;width:960px;text-align:center;font-family:var(--display);font-size:25px;letter-spacing:.5px}

.orb{position:absolute;border-radius:50%;background:var(--orb);text-align:center;display:flex;flex-direction:column;align-items:center}
.orb.lit{background:var(--orb-lit);border:4px solid var(--orb-ring)}
.orb svg{width:48px;height:48px;margin-top:36px}
.orb h3{font-size:15.5px;font-weight:500;margin-top:8px}
.orb p{font-size:11.5px;line-height:18px;color:var(--muted);width:190px;margin-top:12px;text-align:justify;text-align-last:center}
.orb .more{font-size:11.5px;font-weight:700;margin-top:9px;display:flex;gap:6px;align-items:center}

.about-art{left:90px;top:1136px;width:355px;height:327px;border-radius:10px;border-bottom:2px solid var(--violet-deep);
  background:radial-gradient(circle at 50% 40%,#b6d9e8 0%,#5a8fb8 18%,#2c3b6a 42%,#141028 80%)}
.about-title{left:501px;top:1135px;font-family:var(--display);font-size:25px}
.about-copy{left:501px;top:1180px;width:375px;font-size:12px;line-height:21px;color:var(--muted)}
.about-copy p{margin-bottom:11px}
.read-more{left:501px;top:1425px;width:129px;height:33px}
.call-icon{left:657px;top:1427px;width:33px;height:33px;border-radius:50%;background:var(--lime);display:flex;align-items:center;justify-content:center}
.call-label{left:702px;top:1424px;font-size:10px;font-weight:500}
.call-number{left:702px;top:1438px;font-size:18px;color:var(--lime);font-weight:500}

.card{position:absolute;top:1662px;width:246px;height:299px;background:var(--card);text-align:center}
.card .shot{position:absolute;left:6px;top:7px;width:234px;height:141px}
.card h3{position:absolute;top:181px;left:0;width:100%;font-size:14px;font-weight:700}
.card p{position:absolute;top:205px;left:15px;width:216px;font-size:11.5px;line-height:19px;color:var(--muted)}
.card .more{position:absolute;top:257px;left:0;width:100%;font-size:11px;font-weight:700;color:var(--lime);display:flex;justify-content:center;gap:6px;align-items:center}

.field{position:absolute;height:35px;background:var(--field);border:1px solid var(--line);border-radius:3px;font-size:10.5px;display:flex;align-items:center;gap:10px;padding-left:14px}
.field.area{align-items:flex-start;padding-top:14px}
.submit{left:416px;top:2388px;width:127px;height:36px}

.footer-brand{left:90px;top:2583px;font-size:33px}
.signup{left:90px;top:2632px;width:191px;height:27px;border-radius:14px;background:#2a0d36;font-size:8.5px;display:flex;align-items:center;padding-left:16px;gap:8px;overflow:hidden}
.signup .go{position:absolute;right:0;top:0;width:36px;height:27px;background:var(--violet);display:flex;align-items:center;justify-content:center}
.stay{left:90px;top:2682px;font-size:14px;font-weight:700}
.social{top:2710px;width:25px;height:25px;border-radius:50%;background:#fff}
.col{top:2582px;font-size:11px}
.col h4{font-size:13px;font-weight:700;margin-bottom:10px}
.col li{list-style:none;height:24px;display:flex;gap:10px;align-items:center}
.col li::before{content:"»";}
.contact div{display:flex;gap:14px;font-size:11px;line-height:18px;margin-bottom:14px}
.rule{left:90px;top:2772px;width:780px;height:1px;background:var(--line)}
.copy{left:0;top:2796px;width:960px;text-align:center;font-size:11px}
</style>
</head>
<body>

<section class="splash">
  <div role="img" aria-label="Milky way star field in violet and blue" class="abs" style="inset:0;background:transparent"></div>
  <div class="splash-name">LUMOKITT</div>
</section>

<main class="site">
  <header class="nav">
    <div class="brand">LUMOKITT</div>
    <nav class="menu">
      <span class="active">HOME</span><span>ABOUT US</span><span>SERVICES</span><span>WHY CHOOSE US</span><span>CONTACT US</span>
    </nav>
    <svg class="search" width="14" height="14" viewBox="0 0 14 14"><circle cx="6" cy="6" r="4.2" fill="none" stroke="#fff" stroke-width="2"/><path d="M9 9l4 4" stroke="#fff" stroke-width="2"/></svg>
    <div class="btn login">LOGIN <svg viewBox="0 0 12 12"><rect x="2" y="5" width="8" height="6" fill="#fff"/><path d="M4 5V3.5a2 2 0 0 1 4 0V5" fill="none" stroke="#fff" stroke-width="1.5"/></svg></div>
  </header>

  <section class="hero">
    <div class="abs wheel" role="img" aria-label="Glowing zodiac wheel among stars"></div>
    <div class="abs welcome">WELCOME TO</div>
    <h1 class="abs hero-title">LUMOKITT</h1>
    <p class="abs hero-copy">Lorem ipsum dolor sit amet consectetur adipiscing elit sed eiusmod tempor incididun labore et dolore magna aliqud.</p>
    <div class="btn get-started">GET STARTED <svg viewBox="0 0 12 12"><circle cx="6" cy="6" r="6" fill="#fff"/><path d="M5 3.5L7.5 6 5 8.5" fill="none" stroke="#8a14c4" stroke-width="1.6"/></svg></div>
  </section>
  <svg class="hero-curve" viewBox="0 0 960 110" preserveAspectRatio="none"><path d="M0 0 Q480 134 960 0 L960 110 L0 110Z" fill="#12041a"/></svg>

  <h2 class="section" style="top:678px">WHY CHOOSE US</h2>

  <div class="orb" style="left:135px;top:759px;width:228px;height:228px">
    <svg viewBox="0 0 48 48"><ellipse cx="24" cy="24" rx="20" ry="9" transform="rotate(-35 24 24)" fill="none" stroke="#fff" stroke-width="2"/><ellipse cx="24" cy="24" rx="12" ry="5" transform="rotate(-35 24 24)" fill="none" stroke="#fff" stroke-width="2"/><circle cx="24" cy="24" r="3" fill="#fff"/></svg>
    <h3>Lorem ipsum doramet</h3>
    <p>Lorem ipsum dolor consectetur elit, sed do eiusmod tempor incididunt ut labore et dolore magna aliqua.</p>
    <div class="more">LEARN MORE <svg width="11" height="11" viewBox="0 0 12 12"><circle cx="6" cy="6" r="6" fill="#fff"/><path d="M5 3.5L7.5 6 5 8.5" fill="none" stroke="#4a0f66" stroke-width="1.6"/></svg></div>
  </div>
  <div class="orb lit" style="left:355px;top:748px;width:250px;height:250px">
    <svg viewBox="0 0 48 48"><circle cx="24" cy="26" r="11" fill="#fff"/><ellipse cx="24" cy="26" rx="21" ry="6" transform="rotate(-25 24 26)" fill="none" stroke="#fff" stroke-width="2"/><path d="M8 6l1.5 3 3 1.5-3 1.5L8 15l-1.5-3-3-1.5 3-1.5z" fill="#fff"/></svg>
    <h3>Lorem ipsum doramet</h3>
    <p>Lorem ipsum dolor consectetur elit, sed do eiusmod tempor incididunt ut labore et dolore magna aliqua.</p>
    <div class="more">LEARN MORE <svg width="11" height="11" viewBox="0 0 12 12"><circle cx="6" cy="6" r="6" fill="#fff"/><path d="M5 3.5L7.5 6 5 8.5" fill="none" stroke="#3a1896" stroke-width="1.6"/></svg></div>
  </div>
  <div class="orb" style="left:594px;top:759px;width:228px;height:228px">
    <svg viewBox="0 0 48 48"><path d="M14 26l3 7 7 1-5 5 1 7-6-3-6 3 1-7-5-5 7-1z" fill="#fff"/><path d="M22 22L40 4M26 26L44 10M18 18L30 6M30 30l10-10" stroke="#fff" stroke-width="2" stroke-dasharray="4 3"/></svg>
    <h3>Lorem ipsum doramet</h3>
    <p>Lorem ipsum dolor consectetur elit, sed do eiusmod tempor incididunt ut labore et dolore magna aliqua.</p>
    <div class="more">LEARN MORE <svg width="11" height="11" viewBox="0 0 12 12"><circle cx="6" cy="6" r="6" fill="#fff"/><path d="M5 3.5L7.5 6 5 8.5" fill="none" stroke="#4a0f66" stroke-width="1.6"/></svg></div>
  </div>

  <div class="abs about-art" role="img" aria-label="Figure before a luminous astrology wheel"></div>
  <h2 class="abs about-title">ABOUT US</h2>
  <div class="abs about-copy">
    <p>Lorem ipsum dolor sit amet, consectetur adipiscing elit, sed do dolor eiusmod tempor incididunt ut labore et dolore magna aliqua. Ut enim ad minim veniam, quis nostrud exercitation ullamco laboris nisi ut aliquip t labore et dolore magna aliqua commodo consequated.</p>
    <p>Duis aute irure dolor in reprehenderit in voluptate velitt labore et dolore magna aliquadolore eu fugiat nulla pariatur. Excepteur sint occaecat cupidatat non proident, sunt in culpa qui officia id est laborum.</p>
    <p>Lorem ipsum dolor sit amet, consectetur adipiscing elited labore eted dolore magna aliquaeiusmod incididunt ut magna aliqua.</p>
  </div>
  <div class="btn read-more">READ MORE <svg viewBox="0 0 12 12"><circle cx="6" cy="6" r="6" fill="#fff"/><path d="M5 3.5L7.5 6 5 8.5" fill="none" stroke="#8a14c4" stroke-width="1.6"/></svg></div>
  <div class="abs call-icon"><svg width="17" height="17" viewBox="0 0 24 24"><path d="M6.6 10.8a15 15 0 0 0 6.6 6.6l2.2-2.2c.3-.3.7-.4 1-.2 1.1.4 2.3.6 3.6.6.6 0 1 .4 1 1V20c0 .6-.4 1-1 1A17 17 0 0 1 3 4c0-.6.4-1 1-1h3.5c.6 0 1 .4 1 1 0 1.2.2 2.4.6 3.6.1.3 0 .7-.2 1z" fill="#fff"/></svg></div>
  <div class="abs call-label">Call Us Today</div>
  <div class="abs call-number">+1 888 888 8888</div>

  <h2 class="section" style="top:1595px">OUR SERVICES</h2>
  <article class="card" style="left:90px">
    <div class="shot" role="img" aria-label="Illustrated jewelry shop scene" style="background:linear-gradient(160deg,#9a2a6a,#c45a8a 45%,#6a2a86)"></div>
    <h3>Lorem ipsum dolor sit amet</h3>
    <p>Sed ut perspiciatis unde omnis iste natus error sited voluptatem accusantium</p>
    <div class="more">READ MORE <svg width="10" height="10" viewBox="0 0 12 12"><circle cx="6" cy="6" r="6" fill="#59ff00"/><path d="M5 3.5L7.5 6 5 8.5" fill="none" stroke="#22082e" stroke-width="1.6"/></svg></div>
  </article>
  <article class="card" style="left:357px">
    <div class="shot" role="img" aria-label="Planets of the solar system" style="background:radial-gradient(ellipse at 55% 60%,#c9b8c8,#5a4a78 35%,#1c1a3a 75%)"></div>
    <h3>Lorem ipsum dolor sit amet</h3>
    <p>Sed ut perspiciatis unde omnis iste natus error sited voluptatem accusantium</p>
    <div class="more">READ MORE <svg width="10" height="10" viewBox="0 0 12 12"><circle cx="6" cy="6" r="6" fill="#59ff00"/><path d="M5 3.5L7.5 6 5 8.5" fill="none" stroke="#22082e" stroke-width="1.6"/></svg></div>
  </article>
  <article class="card" style="left:625px">
    <div class="shot" role="img" aria-label="Nebula with bright stars" style="background:radial-gradient(ellipse at 50% 55%,#e8d8b8,#8a7a8a 25%,#2a2a4a 60%,#0c0c1c)"></div>
    <h3>Lorem ipsum dolor sit amet</h3>
    <p>Sed ut perspiciatis unde omnis iste natus error sited voluptatem accusantium</p>
    <div class="more">READ MORE <svg width="10" height="10" viewBox="0 0 12 12"><circle cx="6" cy="6" r="6" fill="#59ff00"/><path d="M5 3.5L7.5 6 5 8.5" fill="none" stroke="#22082e" stroke-width="1.6"/></svg></div>
  </article>

  <h2 class="section" style="top:2091px">GET IN TOUCH</h2>
  <div class="field" style="left:128px;top:2148px;width:347px">&#9679; First Name</div>
  <div class="field" style="left:486px;top:2148px;width:347px">&#9679; Last Name</div>
  <div class="field" style="left:128px;top:2199px;width:347px">&#9993; Email</div>
  <div class="field" style="left:486px;top:2199px;width:347px">&#9647; Phone</div>
  <div class="field area" style="left:128px;top:2250px;width:705px;height:116px">&#9679; Comments</div>
  <div class="btn submit">SUBMIT NOW <svg viewBox="0 0 12 12"><circle cx="6" cy="6" r="6" fill="#fff"/><path d="M5 3.5L7.5 6 5 8.5" fill="none" stroke="#8a14c4" stroke-width="1.6"/></svg></div>

  <footer>
    <div class="brand footer-brand">LUMOKITT</div>
    <div class="abs signup">&#9993; Email Address
      <div class="go"><svg width="13" height="13" viewBox="0 0 14 14"><path d="M1 7L13 1 10 13 7 8z" fill="#fff"/></svg></div>
    </div>
    <div class="abs stay">STAY CONNECTED :</div>
    <div class="abs social" style="left:90px"></div>
    <div class="abs social" style="left:121px"></div>
    <div class="abs social" style="left:152px"></div>

    <div class="abs col" style="left:378px"><h4>USEFUL LINKS</h4><ul><li>FAQ</li><li>Privacy</li><li>Policy</li><li>Team</li><li>Contact Us</li></ul></div>
    <div class="abs col" style="left:544px"><h4>QUICK LINKS</h4><ul><li>Home</li><li>About Us</li><li>Services</li><li>why Choose Us</li><li>Contact Us</li></ul></div>
    <div class="abs col contact" style="left:720px"><h4>CONTACT US</h4>
      <div><span>&#9679;</span><span>Lorem ipsum dolor sitm<br>consectetur ardipiscingt.</span></div>
      <div><span>&#9742;</span><span>+1888-888-8888</span></div>
      <div><span>&#9993;</span><span>info@lumokitt.com</span></div>
    </div>
    <div class="abs rule"></div>
    <div class="abs copy">© 2022 LumoKitt &nbsp; | &nbsp; All Rights Reserved &nbsp; | &nbsp; Terms and Conditions</div>
  </footer>
</main>

</body>
</html>
```